Phuket Thailand - Palm Haven Website

I have a villa for rent in Thailand and require a website - i need to demo pictures/walk through video, local attractions, villa facilities description plus seaonal rates and online booking.

Industry/Entity Type

Rental

Coding

Coded - Design and coding required

```html
<!DOCTYPE html>
<html lang="en">
<head>
<meta charset="utf-8">
<title>Palm Haven – Villa Rentals in Phuket</title>
<link rel="stylesheet" href="https://fonts.googleapis.com/css2?family=Questrial&family=Open+Sans:wght@400;600;700&family=Cormorant+Garamond:ital,wght@1,500&display=swap">
<style>
:root{
  --accent:#e59a1c;
  --ink:#333333;
  --muted:#6b6b6b;
  --line:#dcdcdc;
  --blue:#72c3dc;
  --green:#7cb42a;
  --panel:#e3e3e3;
  --footer:#7a7975;
  --footer-dark:#4a4a48;
  --white:#ffffff;
}
*{box-sizing:border-box;margin:0;padding:0}
html,body{width:1200px;height:3137px;overflow:hidden}
body{background:var(--white);font-family:"Open Sans",Arial,sans-serif;color:var(--ink);font-size:13px;position:relative}
.heading-font{font-family:"Questrial",Arial,sans-serif}

/* top bar */
.topbar{height:37px;border-bottom:1px solid var(--line);display:flex;align-items:center;padding:0 86px;font-size:13px;color:var(--muted);gap:22px;position:relative}
.topbar b{font-weight:400;color:var(--accent)}
.topbar .search{position:absolute;right:86px;top:9px}

/* header */
.header{height:78px;display:flex;align-items:center;justify-content:space-between;padding:0 79px 0 80px}
.brand{font-family:"Questrial",Arial,sans-serif;font-size:38px;color:#3a3a3a;letter-spacing:.5px}
.nav{display:flex;gap:22px;font-family:"Questrial",Arial,sans-serif;font-size:15px;color:#333}
.nav a{color:inherit;text-decoration:none;padding-bottom:6px}
.nav a.active{color:var(--accent);border-bottom:3px solid var(--accent)}

/* hero */
.hero{position:relative;height:625px;background:linear-gradient(120deg,#7f8a6a 0%,#d7d8d3 22%,#9a8473 48%,#7a5a4b 70%,#a47c62 100%);overflow:hidden}
.hero-title{position:absolute;left:0;right:0;top:360px;text-align:center;font-family:"Cormorant Garamond",Georgia,serif;font-style:italic;color:var(--white);line-height:1}
.hero-title .l1{font-size:72px;display:block}
.hero-title .l2{font-size:50px;display:block;margin-top:4px}
.hero-ring{position:absolute;left:486px;top:313px;width:236px;height:236px;border:2px solid rgba(255,255,255,.75);border-radius:50%}
.thumbs{position:absolute;left:240px;top:539px;width:720px;height:83px;display:flex;gap:6px;padding:0 2px}
.thumbs .thumb{flex:1;border:2px solid var(--white)}
.thumbs .arrow{position:absolute;top:29px;width:24px;height:24px;border-radius:50%;background:rgba(255,255,255,.85)}
.thumbs .arrow.left{left:-28px}
.thumbs .arrow.right{right:-28px}

/* section headings */
.section-title{display:flex;align-items:center;gap:14px;margin:0 86px;font-family:"Questrial",Arial,sans-serif;font-size:24px;color:#333;text-transform:uppercase}
.section-title::before,.section-title::after{content:"";flex:1;height:1px;background:var(--line)}
.section-title strong{color:var(--accent);font-weight:700;font-family:"Open Sans",Arial,sans-serif;font-size:22px}

/* features */
.features{padding-top:50px}
.feature-row{display:flex;justify-content:space-between;margin:44px 86px 0;position:relative}
.feature-row::before{content:"";position:absolute;left:0;right:0;top:-16px;height:1px;background:var(--line)}
.feature{width:340px;text-align:center}
.feature svg{display:block;margin:0 auto}
.feature h3{font-size:13px;font-weight:700;margin:30px 0 10px;text-transform:uppercase}
.feature p{font-size:12.5px;line-height:1.6;color:var(--muted)}

.divider{height:1px;background:var(--line);margin:40px 86px 0}

/* destinations */
.destinations{padding-top:26px}
.cards{display:grid;grid-template-columns:repeat(4,240px);gap:29px 25px;margin:48px 86px 0}
.card{border:1px solid #e4e4e4;box-shadow:0 1px 4px rgba(0,0,0,.08);height:372px;display:flex;flex-direction:column}
.card-photo{height:220px}
.card-body{padding:13px 10px 0}
.card-body h4{font-size:13px;font-weight:700;line-height:1.4;color:#222}
.price{font-size:12.5px;color:var(--muted);margin-top:18px;padding-bottom:10px;border-bottom:1px solid #ececec}
.card-foot{display:flex;align-items:center;justify-content:space-between;padding:10px 0 0}
.place{display:flex;align-items:center;gap:6px;font-size:12.5px;color:var(--muted)}
.btn-details{background:var(--blue);color:var(--white);font-size:11.5px;padding:7px 9px;text-transform:uppercase}

/* video */
.video{position:relative;height:407px;margin-top:58px;background:linear-gradient(90deg,#3c2d25 0%,#5e4f45 30%,#8e8780 55%,#a7a9a3 80%,#6d6f60 100%);display:flex;flex-direction:column;align-items:center;justify-content:center;gap:20px}
.video::after{content:"";position:absolute;inset:0;background:rgba(0,0,0,.28)}
.video h2{position:relative;z-index:1;font-family:"Open Sans",Arial,sans-serif;font-weight:600;font-size:33px;color:var(--white)}
.video .play{position:relative;z-index:1}

/* booking */
.booking{display:flex;height:340px}
.book-panel{width:604px;background:var(--panel);padding:28px 0 0 94px;margin-left:73px}
.block-title{font-family:"Questrial",Arial,sans-serif;font-size:24px;color:#333;text-transform:uppercase}
.block-title strong{font-family:"Open Sans",Arial,sans-serif;font-weight:700;font-size:22px}
.book-panel .block-title{margin-left:-72px}
.book-form{margin-left:-72px;margin-top:16px;border-top:1px solid #c9c9c9;padding-top:20px;width:475px}
.label{font-size:14px;font-weight:700;color:#333}
.label small{font-weight:400;font-size:14px}
.row{display:flex;gap:10px;margin-top:8px}
.field{background:var(--white);border:1px solid #cfcfcf;height:36px;display:flex;align-items:center;justify-content:space-between;padding:0 8px;font-size:12.5px;color:#444}
.field.muted{color:#999}
.group{display:flex;flex-direction:column}
.groups{display:flex;gap:22px;margin-top:16px}
.btn-book{display:inline-block;background:var(--green);color:var(--white);font-weight:700;font-size:15px;padding:11px 22px;border-radius:3px;margin-top:20px;text-transform:uppercase}
.difference{flex:1;padding:28px 0 0 32px;margin-right:78px}
.difference .list{margin-top:16px;border-top:1px solid var(--line)}
.diff-item{display:flex;gap:16px;margin-top:20px}
.diff-item h5{font-size:15px;font-weight:700;color:#333;text-transform:uppercase}
.diff-item p{font-size:12.5px;line-height:1.55;color:var(--muted);margin-top:6px}

/* footer */
.footer{height:327px;background:var(--footer);color:#f2f2f2;padding:0 86px}
.footer-nav{display:flex;gap:28px;font-size:12.5px;text-transform:uppercase;height:47px;align-items:center;border-bottom:1px solid #939290}
.footer-cols{display:flex;margin-top:34px}
.footer-col h6{font-size:15px;font-weight:600;margin-bottom:4px}
.footer-col p{font-size:12.5px;line-height:1.5}
.col-social{width:265px}
.col-news{width:352px}
.col-about{flex:1}
.socials{display:flex;gap:10px;margin-top:14px}
.socials span{width:32px;height:32px;background:#e8e8e8;border-radius:3px}
.signup{display:flex;margin-top:16px}
.signup .input{width:190px;height:40px;background:#e9e9e9;color:#777;font-size:12px;display:flex;align-items:center;padding:0 10px}
.signup .btn{height:40px;background:var(--footer-dark);color:var(--white);font-size:13px;display:flex;align-items:center;padding:0 14px;text-transform:uppercase}
.footer-bottom{display:flex;justify-content:space-between;margin-top:60px;font-size:12px;color:#e9e9e9}
.footer-bottom .links{display:flex;gap:28px}
</style>
</head>
<body>

<div class="topbar">
  <span>Contact: <b>1-800-555-0148</b></span>
  <span>Email: <b>hello@palmhavenstays.com</b></span>
  <svg class="search" width="18" height="18" viewBox="0 0 18 18"><circle cx="7" cy="7" r="5.5" fill="none" stroke="#333" stroke-width="2"/><line x1="11" y1="11" x2="16.5" y2="16.5" stroke="#333" stroke-width="2.2"/></svg>
</div>

<header class="header">
  <div class="brand">Palm Haven</div>
  <nav class="nav">
    <a class="active">HOME</a><a>ABOUT US</a><a>FACILITIES &amp; SERVICES</a><a>DESTINATIONS</a><a>FEATURED VILLAS</a><a>CONTACT US</a>
  </nav>
</header>

<section class="hero" role="img" aria-label="Photo of a modern villa with a tiled curved roof and garden">
  <div class="hero-ring"></div>
  <div class="hero-title"><span class="l1">Lorem ipsum dolor sit amet</span><span class="l2">consectetur adipiscing elit</span></div>
  <div class="thumbs">
    <span class="arrow left"></span>
    <div class="thumb" role="img" aria-label="Villa roof thumbnail" style="background:linear-gradient(#8a7868,#5f5548)"></div>
    <div class="thumb" role="img" aria-label="Poolside loungers thumbnail" style="background:linear-gradient(#8fb7d1,#5c8a5f)"></div>
    <div class="thumb" role="img" aria-label="Sea view terrace thumbnail" style="background:linear-gradient(#c9dbe6,#89b8cf)"></div>
    <div class="thumb" role="img" aria-label="Infinity pool thumbnail" style="background:linear-gradient(#4f86b8,#2f6ea3)"></div>
    <div class="thumb" role="img" aria-label="Pool at dusk thumbnail" style="background:linear-gradient(#3d7fb0,#2a5d8a)"></div>
    <span class="arrow right"></span>
  </div>
</section>

<section class="features">
  <h2 class="section-title">3 things <strong>you should know</strong> about us</h2>
  <div class="feature-row">
    <div class="feature">
      <svg width="44" height="44" viewBox="0 0 44 44"><circle cx="22" cy="22" r="19" fill="none" stroke="#777" stroke-width="3"/><polygon points="22,10 25.5,18.5 34,19 27.5,25 29.5,33.5 22,29 14.5,33.5 16.5,25 10,19 18.5,18.5" fill="#777"/></svg>
      <h3>Quality. Assured.</h3>
      <p>Lorem ipsum dolor sit amet, consectetur adipiscing elit, sed do eiusmod tempor incididunt ut labore et dolore magna aliqua. Ut enim ad minim veniam, quis nostrud exercitation.</p>
    </div>
    <div class="feature">
      <svg width="48" height="44" viewBox="0 0 48 44"><polygon points="24,3 46,23 40,23 40,42 29,42 29,30 19,30 19,42 8,42 8,23 2,23" fill="#777"/></svg>
      <h3>The perfect match</h3>
      <p>Lorem ipsum dolor sit amet, consectetur adipiscing elit, sed do eiusmod tempor incididunt ut labore et dolore magna aliqua. Ut enim ad minim veniam, quis nostrud exercitation.</p>
    </div>
    <div class="feature">
      <svg width="46" height="46" viewBox="0 0 46 46"><path d="M38 14 A18 18 0 1 1 23 5" fill="none" stroke="#777" stroke-width="3.5"/><polygon points="20,0 30,5 20,11" fill="#777"/><polyline points="23,13 23,24 30,28" fill="none" stroke="#777" stroke-width="3"/></svg>
      <h3>At your service 24/7</h3>
      <p>Lorem ipsum dolor sit amet, consectetur adipiscing elit, sed do eiusmod tempor incididunt ut labore et dolore magna aliqua. Ut enim ad minim veniam, quis nostrud exercitation.</p>
    </div>
  </div>
  <div class="divider"></div>
</section>

<section class="destinations">
  <h2 class="section-title">Popular <strong>destinations</strong></h2>
  <div class="cards">
    <article class="card"><div class="card-photo" role="img" aria-label="Villa pool with palm trees" style="background:linear-gradient(#8fbfe0,#3f8cc2 60%,#6f8b6a)"></div><div class="card-body"><h4>Lorem ipsum dolor sit amet consectetur</h4><div class="price">$850 - $2,950 /night</div><div class="card-foot"><span class="place"><svg width="11" height="15" viewBox="0 0 11 15"><path d="M5.5 0A5.5 5.5 0 0 0 0 5.5C0 9.5 5.5 15 5.5 15S11 9.5 11 5.5A5.5 5.5 0 0 0 5.5 0z" fill="#e59a1c"/><circle cx="5.5" cy="5.5" r="2" fill="#fff"/></svg>Lorem Ipsum</span><span class="btn-details">View details</span></div></div></article>
    <article class="card"><div class="card-photo" role="img" aria-label="Terrace with loungers and sea view" style="background:linear-gradient(#9ec7ea,#4d8fc4 55%,#5b4a3d)"></div><div class="card-body"><h4>Lorem ipsum dolor sit amet consectetur</h4><div class="price">$850 - $2,950 /night</div><div class="card-foot"><span class="place"><svg width="11" height="15" viewBox="0 0 11 15"><path d="M5.5 0A5.5 5.5 0 0 0 0 5.5C0 9.5 5.5 15 5.5 15S11 9.5 11 5.5A5.5 5.5 0 0 0 5.5 0z" fill="#e59a1c"/><circle cx="5.5" cy="5.5" r="2" fill="#fff"/></svg>Lorem Ipsum</span><span class="btn-details">View details</span></div></div></article>
    <article class="card"><div class="card-photo" role="img" aria-label="Thatched villa by an infinity pool" style="background:linear-gradient(#b7cfe3,#7a7766 50%,#3f86b3)"></div><div class="card-body"><h4>Lorem ipsum dolor sit amet consectetur</h4><div class="price">$850 - $2,950 /night</div><div class="card-foot"><span class="place"><svg width="11" height="15" viewBox="0 0 11 15"><path d="M5.5 0A5.5 5.5 0 0 0 0 5.5C0 9.5 5.5 15 5.5 15S11 9.5 11 5.5A5.5 5.5 0 0 0 5.5 0z" fill="#e59a1c"/><circle cx="5.5" cy="5.5" r="2" fill="#fff"/></svg>Lorem Ipsum</span><span class="btn-details">View details</span></div></div></article>
    <article class="card"><div class="card-photo" role="img" aria-label="Pool deck with blue sun loungers" style="background:linear-gradient(#a9d0ef,#5a9fd0 55%,#2e78b3)"></div><div class="card-body"><h4>Lorem ipsum dolor sit amet consectetur</h4><div class="price">$850 - $2,950 /night</div><div class="card-foot"><span class="place"><svg width="11" height="15" viewBox="0 0 11 15"><path d="M5.5 0A5.5 5.5 0 0 0 0 5.5C0 9.5 5.5 15 5.5 15S11 9.5 11 5.5A5.5 5.5 0 0 0 5.5 0z" fill="#e59a1c"/><circle cx="5.5" cy="5.5" r="2" fill="#fff"/></svg>Lorem Ipsum</span><span class="btn-details">View details</span></div></div></article>
    <article class="card"><div class="card-photo" role="img" aria-label="White modern villa with turquoise pool" style="background:linear-gradient(#c4d8e6,#d9d9d4 45%,#3fb4b0)"></div><div class="card-body"><h4>Lorem ipsum dolor sit amet consectetur</h4><div class="price">$850 - $2,950 /night</div><div class="card-foot"><span class="place"><svg width="11" height="15" viewBox="0 0 11 15"><path d="M5.5 0A5.5 5.5 0 0 0 0 5.5C0 9.5 5.5 15 5.5 15S11 9.5 11 5.5A5.5 5.5 0 0 0 5.5 0z" fill="#e59a1c"/><circle cx="5.5" cy="5.5" r="2" fill="#fff"/></svg>Lorem Ipsum</span><span class="btn-details">View details</span></div></div></article>
    <article class="card"><div class="card-photo" role="img" aria-label="Infinity pool at sunset over the bay" style="background:linear-gradient(#8c9fc8,#c7a9b6 45%,#3a6fa8)"></div><div class="card-body"><h4>Lorem ipsum dolor sit amet consectetur</h4><div class="price">$850 - $2,950 /night</div><div class="card-foot"><span class="place"><svg width="11" height="15" viewBox="0 0 11 15"><path d="M5.5 0A5.5 5.5 0 0 0 0 5.5C0 9.5 5.5 15 5.5 15S11 9.5 11 5.5A5.5 5.5 0 0 0 5.5 0z" fill="#e59a1c"/><circle cx="5.5" cy="5.5" r="2" fill="#fff"/></svg>Lorem Ipsum</span><span class="btn-details">View details</span></div></div></article>
    <article class="card"><div class="card-photo" role="img" aria-label="Tropical garden pool with frangipani tree" style="background:linear-gradient(#a8c4dc,#56705a 45%,#2f6f9e)"></div><div class="card-body"><h4>Lorem ipsum dolor sit amet consectetur</h4><div class="price">$850 - $2,950 /night</div><div class="card-foot"><span class="place"><svg width="11" height="15" viewBox="0 0 11 15"><path d="M5.5 0A5.5 5.5 0 0 0 0 5.5C0 9.5 5.5 15 5.5 15S11 9.5 11 5.5A5.5 5.5 0 0 0 5.5 0z" fill="#e59a1c"/><circle cx="5.5" cy="5.5" r="2" fill="#fff"/></svg>Lorem Ipsum</span><span class="btn-details">View details</span></div></div></article>
    <article class="card"><div class="card-photo" role="img" aria-label="Hillside villa terrace overlooking the sea" style="background:linear-gradient(#bcd3e4,#8d7a62 50%,#4b6b4a)"></div><div class="card-body"><h4>Lorem ipsum dolor sit amet consectetur</h4><div class="price">$850 - $2,950 /night</div><div class="card-foot"><span class="place"><svg width="11" height="15" viewBox="0 0 11 15"><path d="M5.5 0A5.5 5.5 0 0 0 0 5.5C0 9.5 5.5 15 5.5 15S11 9.5 11 5.5A5.5 5.5 0 0 0 5.5 0z" fill="#e59a1c"/><circle cx="5.5" cy="5.5" r="2" fill="#fff"/></svg>Lorem Ipsum</span><span class="btn-details">View details</span></div></div></article>
  </div>
</section>

<section class="video" role="img" aria-label="Video still of a villa bedroom interior with artwork and a view of the garden">
  <h2>WATCH VIDEO</h2>
  <svg class="play" width="96" height="74" viewBox="0 0 96 74"><rect width="96" height="74" rx="14" fill="#fff"/><polygon points="38,20 38,54 64,37" fill="#222"/></svg>
</section>

<section class="booking">
  <div class="book-panel">
    <h2 class="block-title">Book <strong>now</strong></h2>
    <div class="book-form">
      <div class="label">Find a rental</div>
      <div class="row">
        <div class="field" style="width:185px">Phuket, Thailand</div>
        <div class="field muted" style="width:130px">Check in <svg width="18" height="16" viewBox="0 0 18 16"><rect x="1" y="2" width="16" height="13" fill="#888"/><rect x="3" y="6" width="12" height="7" fill="#ddd"/></svg></div>
        <div class="field muted" style="width:130px">Check out <svg width="18" height="16" viewBox="0 0 18 16"><rect x="1" y="2" width="16" height="13" fill="#888"/><rect x="3" y="6" width="12" height="7" fill="#ddd"/></svg></div>
      </div>
      <div class="groups">
        <div class="group"><div class="label">Bedrooms</div><div class="row"><div class="field" style="width:112px">Any <svg width="10" height="6"><polygon points="0,0 10,0 5,6" fill="#555"/></svg></div></div></div>
        <div class="group"><div class="label">Amenities</div><div class="row"><div class="field" style="width:112px">Select <svg width="10" height="6"><polygon points="0,0 10,0 5,6" fill="#555"/></svg></div></div></div>
        <div class="group"><div class="label">Price <small>per night</small></div><div class="row"><div class="field" style="width:106px">Min <svg width="10" height="6"><polygon points="0,0 10,0 5,6" fill="#555"/></svg></div><div class="field" style="width:106px">Max <svg width="10" height="6"><polygon points="0,0 10,0 5,6" fill="#555"/></svg></div></div></div>
      </div>
      <span class="btn-book">Book now</span>
    </div>
  </div>
  <div class="difference">
    <h2 class="block-title">The Palm Haven <strong>difference</strong></h2>
    <div class="list">
      <div class="diff-item">
        <svg width="46" height="46" viewBox="0 0 46 46"><circle cx="23" cy="23" r="20" fill="none" stroke="#e59a1c" stroke-width="3"/><circle cx="16" cy="18" r="2.5" fill="#e59a1c"/><circle cx="30" cy="18" r="2.5" fill="#e59a1c"/><path d="M13 26 Q23 36 33 26" fill="none" stroke="#e59a1c" stroke-width="3"/></svg>
        <div><h5>99% customer satisfaction</h5><p>Lorem ipsum dolor sit amet, consectetur adipiscing elit, sed do eiusmod tempor incididunt</p></div>
      </div>
      <div class="diff-item">
        <svg width="46" height="46" viewBox="0 0 46 46"><circle cx="23" cy="23" r="20" fill="none" stroke="#e59a1c" stroke-width="3"/><text x="23" y="28" text-anchor="middle" font-family="Open Sans, sans-serif" font-weight="700" font-size="14" fill="#e59a1c">25+</text></svg>
        <div><h5>Over 25 years experience</h5><p>Lorem ipsum dolor sit amet, consectetur adipiscing elit, sed do eiusmod tempor incididunt</p></div>
      </div>
      <div class="diff-item">
        <svg width="46" height="46" viewBox="0 0 46 46"><rect x="8" y="6" width="28" height="36" rx="3" fill="#e59a1c"/><rect x="16" y="3" width="12" height="7" rx="2" fill="#c27e10"/><polyline points="15,25 21,31 31,19" fill="none" stroke="#fff" stroke-width="3.5"/></svg>
        <div><h5>Personally inspected villas</h5><p>Lorem ipsum dolor sit amet, consectetur adipiscing elit, sed do eiusmod tempor incididunt</p></div>
      </div>
    </div>
  </div>
</section>

<footer class="footer">
  <nav class="footer-nav"><span>Home</span><span>About us</span><span>Destinations</span><span>Featured villas</span><span>Contact us</span></nav>
  <div class="footer-cols">
    <div class="footer-col col-social">
      <h6>Let's Socialize</h6>
      <p>Follow us:</p>
      <div class="socials"><span></span><span></span><span></span><span></span></div>
    </div>
    <div class="footer-col col-news">
      <h6>Stay in the Know</h6>
      <p>Exclusive news &amp; offers straight to your inbox</p>
      <div class="signup"><div class="input">Enter email address...</div><div class="btn">Sign up</div></div>
    </div>
    <div class="footer-col col-about">
      <h6>Who we are</h6>
      <p>Our family has welcomed guests to hand-picked island villas for years, pairing private pools and sea views with caring local hosts, daily housekeeping and tailored tours so every stay feels relaxed, easy and truly your own home away.</p>
    </div>
  </div>
  <div class="footer-bottom">
    <span>Copyright ©2015 Palm Haven. All Rights Reserved.</span>
    <span class="links"><span>Privacy policy</span><span>Terms of use</span></span>
  </div>
</footer>

</body>
</html>
```